Flyer To Solicit Donations for a Good Cause

Hi. I am running the distance of a marathon race to solicit donations for a charitable cause. I need a well designed flyer to help me solicit support from friends and others. The copy for the flyer is attached. There is a significant amount of written text so it will need to be laid out in a way that is easy to read but also mixes well with some good images and design appeal. I am open to creative ideas. I have also attached my photo and a photo of me shaking hands with Mayor Velidis of Delphi and president of the Concordant Aegean Fellowship. Also there are some photos of the areas. These photos don't have to be used except for the one of me shaking hands with the Mayor and a caption underneath it. Otherwise, I am open to other stock photos or graphics. Feel free to contact me if you have questions. Thank you !

Update: ONE SIDED FLYER

Requirements
Must have
• Photo of the Mayor and Dale with the caption identifying us; All of the copy/text.

```html
<!DOCTYPE html>
<html lang="en">
<head>
<meta charset="utf-8">
<title>A Special Journey – Prayer Run Flyer</title>
<link href="https://fonts.googleapis.com/css2?family=Fira+Sans+Condensed:ital,wght@0,300;0,400;0,600;0,700;1,300;1,400;1,500&display=swap" rel="stylesheet">
<style>
  :root{
    --page:#e9e6e2;
    --blue:#1f6db5;
    --orange:#e8891a;
    --white:#ffffff;
    --ink:#1c1c1c;
    --panel:rgba(28,30,34,.72);
  }
  *{box-sizing:border-box;margin:0;padding:0}
  html,body{width:1200px;height:1200px;overflow:hidden;background:var(--page)}
  body{font-family:"Fira Sans Condensed",sans-serif;color:var(--white)}
  .flyer{position:absolute;left:200px;top:35px;width:800px;height:1130px;background:var(--white);overflow:hidden;box-shadow:0 2px 10px rgba(0,0,0,.15)}

  /* hero */
  .hero{position:absolute;left:0;top:0;width:800px;height:425px}
  .hero-runners{position:absolute;left:0;top:0;width:420px;height:425px;
    background:linear-gradient(160deg,#2a78c0 0%,#2366a9 45%,#4f7fa8 75%,#7d8fa0 100%)}
  .hero-ruins{position:absolute;left:420px;top:0;width:380px;height:425px;
    background:linear-gradient(180deg,#b9b9b9 0%,#8e8e8e 35%,#6f6f6f 60%,#8a8a8a 100%)}
  .hero-portrait{position:absolute;left:290px;top:48px;width:265px;height:377px;border-radius:120px 120px 0 0;
    background:linear-gradient(180deg,#3a3f4a 0%,#262b36 40%,#1d2230 100%)}
  .hero-title{position:absolute;left:34px;top:78px;line-height:1.2}
  .hero-title .lead{font-size:40px;font-weight:700;letter-spacing:-.3px}
  .hero-title .sub{font-size:29px;font-weight:300;display:block}
  .hero-name{position:absolute;left:40px;top:322px;font-size:40px;font-weight:700}
  .hero-date{position:absolute;left:40px;top:375px;font-size:27px;font-weight:600}
  .contact{position:absolute;left:466px;top:44px;display:flex;align-items:center;gap:14px;font-size:20px;font-weight:600}

  /* story */
  .story{position:absolute;left:0;top:425px;width:800px;height:400px;
    background:linear-gradient(180deg,#8da0b3 0%,#6f8494 25%,#5e7358 55%,#4f6640 80%,#6d7d5a 100%)}
  .story-text{position:absolute;left:18px;top:12px;width:414px;display:flex;flex-direction:column;gap:10px}
  .panel{background:var(--panel)}
  .panel-head{background:var(--orange);font-size:16px;font-weight:700;line-height:1.25;padding:5px 8px}
  .panel-body{font-size:12.5px;line-height:1.36;padding:6px 8px 8px}
  .panel-body p+p{margin-top:4px}
  .panel-link{font-size:16px;font-weight:600;margin-top:6px}
  .handshake{position:absolute;left:482px;top:24px;width:280px;height:280px;border-radius:50%;border:5px solid var(--white);
    background:linear-gradient(180deg,#c9d6e2 0%,#a9bfd3 40%,#5b6f88 75%,#2f3d55 100%)}
  .caption{position:absolute;left:440px;top:326px;width:350px;background:var(--orange);font-size:14px;font-weight:600;text-align:center;line-height:1.3;padding:5px 8px}

  /* steps */
  .steps{position:absolute;left:22px;top:836px;width:760px;color:var(--ink);font-size:13.5px;font-style:italic;font-weight:500;line-height:1.4;list-style:none;counter-reset:step}
  .steps li{counter-increment:step;padding-left:22px;position:relative;margin-bottom:3px}
  .steps li::before{content:counter(step) ")";position:absolute;left:0}

  /* footer */
  .tagline{position:absolute;left:0;top:1030px;width:800px;height:100px;background:var(--blue);display:flex;align-items:center;justify-content:center;
    font-size:30px;font-weight:300;font-style:italic}
</style>
</head>
<body>
<main class="flyer">
  <section class="hero">
    <div class="hero-runners" role="img" aria-label="Faded photo of runners' legs on a road, tinted blue"></div>
    <div class="hero-ruins" role="img" aria-label="Black and white photo of the circular temple ruins at Delphi with mountains behind"></div>
    <div class="hero-portrait" role="img" aria-label="Photo of Dale Hartwell standing in a dark blazer and striped shirt"></div>
    <h1 class="hero-title"><span class="lead">A Special Journey</span>
      <span class="sub">For Your Specific Prayers</span>
      <span class="sub">&amp; For An Important</span>
      <span class="sub">Ancient Cause</span>
      <span class="sub">By</span></h1>
    <div class="hero-name">Dale Hartwell</div>
    <div class="hero-date">April 2016</div>
    <div class="contact">
      <svg width="34" height="22" viewBox="0 0 34 22" aria-hidden="true"><rect x="1" y="1" width="32" height="20" fill="none" stroke="#fff" stroke-width="2"/><path d="M1 1 L17 13 L33 1" fill="none" stroke="#fff" stroke-width="2"/></svg>
      <span>dhartwell@hartwellmarsh.com</span>
    </div>
  </section>

  <section class="story" role="img" aria-label="Landscape photo of the green mountain valley below Delphi">
    <div class="story-text">
      <div class="panel panel-intro">
        <h2 class="panel-head">This coming April 2016 Dale Hartwell will make a special running journey of 26 miles</h2>
        <div class="panel-body">
          <p>through the ancient lands of Apollo and Athena at Delphi on Mt. Parnassus in Greece.</p>
          <p>Dale will adorn his running outfit with special cloth strips that will contain written prayers and petitions of people who will sponsor his journey by making a charitable donation to the Concordant Aegean Fellowship, an organization that preserves the land and the Delphic culture.</p>
          <p class="panel-link">www.concordant-aegean-fellowship.org</p>
        </div>
      </div>
      <div class="panel panel-concept">
        <h2 class="panel-head">The concept is simple and very powerful</h2>
        <div class="panel-body">
          <p>as Dale runs, your written prayer on a cloth strip will flow and emanate in the wind — being blessed by the spirits of this ancient and magical land — asking unto the wind that your prayer be answered. This type of prayer practice dates back to ancient times. The Tibetan culture commonly uses prayer flags with special mantras and symbols.</p>
          <p>Will you make a prayer for yourself or a loved and support a good cause? Here is how to get your prayer started:</p>
        </div>
      </div>
    </div>
    <div class="handshake" role="img" aria-label="Photo of Dale shaking hands with Mayor Velidis in front of a painted mural"></div>
    <p class="caption">Dale with Mayor Velidis of Delphi and president of the Concordant Aegean Fellowship</p>
  </section>

  <ol class="steps">
    <li>Decide what you want your prayer, petition or intention to be.</li>
    <li>Define your prayer, petition or intention by writing it down.</li>
    <li>Refine it is concise, clear &amp; specific. (18 words or less is ideal for each strip cloth).</li>
    <li>Contact Dale at dhartwell@hartwellmarsh.com and tell him how many prayer cloth strips you wish to obtain. Dale will then send you the cloth for you to write your prayer and send back to him or he will write out the prayer for you. Dale can also answer any questions you may have.</li>
    <li>A minimum donation of $50 for each prayer cloth is requested. Checks can be made to the “Hartwell Marsh Trust Account/Concordant Aegean Fellowship” and mail to Dale T. Hartwell, Hartwell Marsh PLC, 1480 Linden Avenue, Ste. 204 Fairview, Virginia 23000 or though online payment instructions sent by email from Dale as requested.</li>
  </ol>

  <footer class="tagline">Your Prayer Can Make A Difference For You &amp; For A Good Cause !</footer>
</main>
</body>
</html>
```